Home Design company focused on remodel and enhancement of kitchens and bathroorms

I already have a logo designed by ArtHarbor, I now need a design for my business cards.
The company is in the remodeling and enhancement industry for homes, focusing on kitchens and bathrooms, however, we can remodel or enhance every room in a home, an office space, etc.

The company's name is VELMOR HOME DESIGN, LLC

We'll focus on clients in the Rio Grande Valley, Texas. Primarily McAllen, Edinburg, Pharr, Mission, Brownsville and South Padre Island.

The design on the business card should transmit reliability, professionalism anda bit of upscale design.

The logo is in black and white, and would like to keep it that way.

The information that needs to be printed in the business cards is:
Company's name: Velmor Home Design
Company's Logo (attached)
My name: Noel Bramwit
Address, phone and email:
2715 N Parkline Road, Ste 348
Larkfield, ST 00000
(555) 010 0187
nbramwit@velmordesign.example
Website: velmordesign.example

```html
<!DOCTYPE html>
<html lang="en">
<head>
<meta charset="utf-8">
<title>Velmor Home Design — Business Card</title>
<link href="https://fonts.googleapis.com/css2?family=Jost:wght@300;400;600&display=swap" rel="stylesheet">
<style>
  :root {
    --backdrop: #d6d6d6;
    --card-white: #ffffff;
    --ink: #111111;
    --card-black: #0b0b0b;
    --pattern-grey: #3a3838;
    --rule: #222222;
  }
  html, body {
    margin: 0;
    padding: 0;
    width: 1200px;
    height: 846px;
    overflow: hidden;
    background: var(--backdrop);
    font-family: "Jost", "Futura", sans-serif;
    color: var(--ink);
  }
  .canvas {
    position: relative;
    width: 1200px;
    height: 846px;
  }
  .card {
    position: absolute;
    top: 254px;
    width: 520px;
    height: 338px;
    box-shadow: 0 10px 24px rgba(0,0,0,0.18);
  }
  .card--front {
    left: 50px;
    background: var(--card-white);
    display: flex;
    align-items: center;
  }
  .card--back {
    left: 630px;
    background: radial-gradient(ellipse at 55% 50%, var(--pattern-grey) 0%, #1a1919 45%, var(--card-black) 80%);
  }
  .brand {
    width: 150px;
    display: flex;
    align-items: center;
    justify-content: center;
    gap: 10px;
    margin-left: 28px;
  }
  .brand__mark {
    width: 14px;
    height: 14px;
    background: var(--ink);
  }
  .brand__name {
    font-weight: 400;
    font-size: 13px;
    letter-spacing: 2.5px;
    line-height: 1.25;
    text-transform: uppercase;
  }
  .divider {
    width: 1px;
    height: 170px;
    background: var(--rule);
    margin: 0 24px 0 14px;
  }
  .contact__name {
    font-weight: 600;
    font-size: 24px;
    margin: 0 0 10px;
  }
  .contact__list {
    list-style: none;
    margin: 0;
    padding: 0;
  }
  .contact__item {
    display: flex;
    align-items: flex-start;
    gap: 10px;
    font-weight: 300;
    font-size: 15.5px;
    line-height: 1.25;
    margin-bottom: 5px;
  }
  .contact__icon {
    width: 17px;
    height: 17px;
    flex: none;
    margin-top: 1px;
  }
</style>
</head>
<body>
<main class="canvas">
  <section class="card card--front" aria-label="Business card front">
    <div class="brand">
      <span class="brand__mark"></span>
      <span class="brand__name">Velmor<br>Home<br>Design</span>
    </div>
    <div class="divider"></div>
    <div class="contact">
      <h1 class="contact__name">Noel Bramwit</h1>
      <ul class="contact__list">
        <li class="contact__item">
          <svg class="contact__icon" viewBox="0 0 24 24"><rect x="6" y="2" width="12" height="20" rx="2" fill="none" stroke="#111" stroke-width="1.8"/><line x1="10" y1="18.5" x2="14" y2="18.5" stroke="#111" stroke-width="1.8"/></svg>
          <span>(555) 010 0187</span>
        </li>
        <li class="contact__item">
          <svg class="contact__icon" viewBox="0 0 24 24"><rect x="2" y="5" width="20" height="14" fill="#111"/><polyline points="2,5 12,13 22,5" fill="none" stroke="#fff" stroke-width="1.5"/></svg>
          <span>nbramwit@velmordesign.example</span>
        </li>
        <li class="contact__item">
          <svg class="contact__icon" viewBox="0 0 24 24"><circle cx="12" cy="12" r="10" fill="#111"/><g fill="none" stroke="#fff" stroke-width="1.2"><ellipse cx="12" cy="12" rx="4" ry="10"/><line x1="2" y1="12" x2="22" y2="12"/><line x1="12" y1="2" x2="12" y2="22"/><path d="M4 7h16M4 17h16"/></g></svg>
          <span>www.velmordesign.example</span>
        </li>
        <li class="contact__item">
          <svg class="contact__icon" viewBox="0 0 24 24"><path d="M12 1.5a7.5 7.5 0 0 0-7.5 7.5c0 5.5 7.5 13.5 7.5 13.5s7.5-8 7.5-13.5A7.5 7.5 0 0 0 12 1.5z" fill="#111"/><circle cx="12" cy="9" r="2.8" fill="#fff"/></svg>
          <span>2715 N Parkline Road, Ste 348<br>Larkfield, ST 00000</span>
        </li>
      </ul>
    </div>
  </section>

  <section class="card card--back" role="img" aria-label="Black card back with a repeating pattern of the company mark and name in soft grey"></section>
</main>
</body>
</html>
```